KRV In Home Flier

To prepare a flier to be placed directly into existing clients homes, which shares additional services available. These are clients that are using KRV Cleaning services and we want to use our KRV Pest Control or BMO (Bravo Mend On)Maintenance Services

Target Market(s)

residential home owners / Renters

Industry/Entity Type

Property Maintenance

Colors

Designer to choose colors to be used in the design.

Requirements
Must have
• Must be crisp and clean - design should pop - A CLEAR call to action
Nice to have
• See previous designed uploaded
Should not have

```html
<!DOCTYPE html>
<html lang="en">
<head>
<meta charset="utf-8">
<title>KRV Pest Control Flier</title>
<link href="https://fonts.googleapis.com/css2?family=Montserrat:wght@300;400;600;700;800&display=swap" rel="stylesheet">
<style>
  :root {
    --blue: #1a6fc1;
    --blue-deep: #0f5aa6;
    --red: #d8232a;
    --red-soft: #e2454b;
    --ink: #2b2b2b;
    --grey: #e9ebee;
    --white: #ffffff;
    --page: #eceef1;
  }
  * { margin: 0; padding: 0; box-sizing: border-box; }
  html, body { width: 1200px; height: 1200px; overflow: hidden; }
  body { background: var(--page); font-family: "Montserrat", sans-serif; color: var(--ink); }

  .flier {
    position: absolute; left: 190px; top: 20px; width: 820px; height: 1160px;
    background: var(--white); overflow: hidden; box-shadow: 0 6px 24px rgba(0,0,0,.12);
  }
  .hero-photo {
    position: absolute; left: 230px; top: 0; width: 660px; height: 520px;
    border-radius: 0 0 330px 0;
    background: linear-gradient(135deg, #f4f6f9 0%, #dfe4ea 45%, #b9c3cf 100%);
  }
  .hero-ring {
    position: absolute; left: 230px; top: -20px; width: 620px; height: 560px;
    border-right: 10px solid var(--blue); border-bottom: 10px solid transparent;
    border-radius: 0 0 330px 0; pointer-events: none;
  }
  .brand { position: absolute; left: 40px; top: 40px; display: flex; align-items: center; gap: 10px; }
  .brand-dot { width: 34px; height: 34px; border-radius: 50%; background: var(--ink); }
  .brand-name { font-weight: 700; font-size: 22px; color: var(--blue); }

  .title-disc {
    position: absolute; left: -70px; top: 150px; width: 500px; height: 420px;
    border-radius: 50%; background: var(--blue);
    box-shadow: 0 0 0 6px var(--white), 0 0 0 9px var(--blue);
  }
  .title { position: absolute; left: 50px; top: 210px; color: var(--white); line-height: 1; }
  .title .t1 { font-weight: 800; font-size: 78px; letter-spacing: 2px; }
  .title .t2 { font-weight: 300; font-size: 50px; letter-spacing: 3px; margin-top: 4px; }
  .title .t3 { font-weight: 300; font-size: 50px; letter-spacing: 3px; margin-top: 2px; }
  .title-note {
    position: absolute; left: 60px; top: 420px; width: 300px; color: var(--white);
    font-size: 14px; font-weight: 600; line-height: 1.35;
  }

  .thumb { position: absolute; width: 130px; height: 130px; border-radius: 50%; border: 5px solid var(--white); box-shadow: 0 2px 8px rgba(0,0,0,.2); }
  .thumb-a { left: 640px; top: 230px; background: linear-gradient(135deg, #eef1f4, #c9a94a); }
  .thumb-b { left: 560px; top: 340px; background: linear-gradient(135deg, #eef1f4, #b07d4f); }
  .thumb-c { left: 440px; top: 420px; background: linear-gradient(135deg, #d7d9d2, #7a7a66); }

  .services { position: absolute; left: 40px; top: 580px; width: 760px; height: 220px; }
  .service { position: absolute; display: flex; align-items: center; gap: 14px; font-size: 15px; font-weight: 600; white-space: nowrap; }
  .service svg { width: 40px; height: 40px; }

  .badge {
    position: absolute; left: 590px; top: 632px; width: 190px; height: 170px; border-radius: 50%;
    background: var(--red); color: var(--white); text-align: center; padding-top: 28px;
    box-shadow: inset 0 0 0 5px var(--red), inset 0 0 0 7px rgba(255,255,255,.7);
    font-weight: 800; line-height: 1;
  }
  .badge .b1 { font-size: 22px; }
  .badge .b2 { font-size: 15px; margin-top: 2px; }
  .badge .b3 { font-size: 30px; margin-top: 2px; }
  .badge .b3 small { font-size: 16px; }
  .badge .b4 { font-size: 28px; margin-top: 2px; }

  .support {
    position: absolute; left: 540px; top: 820px; width: 280px; height: 340px;
    border-radius: 280px 0 0 0 / 220px 0 0 0; background: var(--blue); color: var(--white);
    box-shadow: 0 0 0 12px var(--grey);
  }
  .support-body { position: absolute; left: 40px; top: 118px; font-size: 14px; font-weight: 600; white-space: nowrap; }
  .support-body h3 { font-size: 14px; font-weight: 700; margin-bottom: 12px; }
  .support-row { display: flex; align-items: center; gap: 10px; margin-bottom: 8px; }
  .support-row svg { width: 16px; height: 16px; }

  .pitch { position: absolute; left: 40px; top: 830px; width: 470px; font-size: 16px; font-weight: 600; line-height: 1.35; }
  .pitch p + p { margin-top: 22px; padding-top: 18px; border-top: 2px solid var(--grey); }

  .cta-band { position: absolute; left: 0; top: 1030px; width: 540px; height: 130px; background: var(--grey); }
  .cta-ribbon {
    position: absolute; left: 0; top: 1070px; width: 262px; height: 66px; background: var(--red-soft);
    clip-path: polygon(0 0, 100% 0, 92% 50%, 100% 100%, 0 100%);
    color: var(--white); font-weight: 800; font-size: 15px; line-height: 1.1; padding: 14px 0 0 30px;
  }
  .cta-phone { position: absolute; left: 278px; top: 1082px; display: flex; align-items: center; gap: 8px; font-weight: 800; font-size: 26px; white-space: nowrap; }
  .cta-phone svg { width: 26px; height: 26px; }
</style>
</head>
<body>
<main class="flier">
  <div class="hero-photo" role="img" aria-label="Photo of a technician in protective suit spraying pest treatment indoors"></div>
  <div class="hero-ring"></div>

  <div class="brand"><span class="brand-dot"></span><span class="brand-name">KRV Pest Control</span></div>

  <div class="title-disc"></div>
  <h1 class="title"><div class="t1">PEST</div><div class="t2">CONTROL</div><div class="t3">SERVICE</div></h1>
  <p class="title-note">European Managed MONTHLY - QUARTERLY - ANNUALLY maintenance contracts On call service Your property, our priority.</p>

  <div class="thumb thumb-a" role="img" aria-label="Photo of technician inspecting a kitchen with a client"></div>
  <div class="thumb thumb-b" role="img" aria-label="Photo of technician treating a wooden floor"></div>
  <div class="thumb thumb-c" role="img" aria-label="Photo of spraying along an exterior wall"></div>

  <section class="services">
    <div class="service" style="left:0;top:110px"><svg viewBox="0 0 40 40"><circle cx="20" cy="20" r="18" fill="none" stroke="#1a6fc1" stroke-width="2"/><circle cx="20" cy="20" r="6" fill="#1a6fc1"/></svg>General Pest Control</div>
    <div class="service" style="left:20px;top:170px"><svg viewBox="0 0 40 40"><circle cx="20" cy="20" r="18" fill="none" stroke="#1a6fc1" stroke-width="2"/><circle cx="20" cy="20" r="6" fill="#1a6fc1"/></svg>Cockroaches Control</div>
    <div class="service" style="left:300px;top:20px"><svg viewBox="0 0 40 40"><circle cx="20" cy="20" r="18" fill="none" stroke="#1a6fc1" stroke-width="2"/><circle cx="20" cy="20" r="6" fill="#1a6fc1"/></svg>Bed Bugs Control</div>
    <div class="service" style="left:320px;top:80px"><svg viewBox="0 0 40 40"><circle cx="20" cy="20" r="18" fill="none" stroke="#1a6fc1" stroke-width="2"/><circle cx="20" cy="20" r="6" fill="#1a6fc1"/></svg>Rat Control</div>
    <div class="service" style="left:560px;top:-10px"><svg viewBox="0 0 40 40"><circle cx="20" cy="20" r="18" fill="none" stroke="#1a6fc1" stroke-width="2"/><circle cx="20" cy="20" r="6" fill="#1a6fc1"/></svg>Ant Control</div>
  </section>

  <div class="badge"><div class="b1">SPECIAL</div><div class="b2">INCENTIVE</div><div class="b3"><small>for</small> KRV</div><div class="b4">CLIENT</div></div>

  <section class="pitch">
    <p>KRV Pest Control is reinventing the pest control service industry in Dubai</p>
    <p>This means you get the right Pest Control Workers, with the right tools at the right time!</p>
  </section>

  <aside class="support">
    <div class="support-body">
      <h3>24/7 CUSTOMER SUPPORT</h3>
      <div class="support-row"><svg viewBox="0 0 24 24"><path d="M6 3l4 4-2 3c1 2 3 4 5 5l3-2 4 4-3 3C10 20 4 14 3 6z" fill="none" stroke="#fff" stroke-width="2"/></svg>+971 04 555 0142</div>
      <div class="support-row"><svg viewBox="0 0 24 24"><path d="M6 3l4 4-2 3c1 2 3 4 5 5l3-2 4 4-3 3C10 20 4 14 3 6z" fill="#fff"/></svg>+971 56 555 0187</div>
      <div class="support-row"><svg viewBox="0 0 24 24"><circle cx="12" cy="12" r="9" fill="none" stroke="#fff" stroke-width="2"/><path d="M3 12h18M12 3c3 3 3 15 0 18M12 3c-3 3-3 15 0 18" fill="none" stroke="#fff" stroke-width="1.5"/></svg>www.krvhomecare.com</div>
    </div>
  </aside>

  <div class="cta-band"></div>
  <div class="cta-ribbon">CALL US NOW FOR A<br>FREE ESTIMATE!</div>
  <div class="cta-phone"><svg viewBox="0 0 24 24"><path d="M6 3l4 4-2 3c1 2 3 4 5 5l3-2 4 4-3 3C10 20 4 14 3 6z" fill="#1a6fc1"/></svg>800 Tidyhome</div>
</main>
</body>
</html>
```